CREATE R&B MIXTAPE COVER !!
Hi , my name is Brontel , and I want you to create a cover for my music mixtape.
The name of the mixtape is Tormenta , and has these types of music :
- R&B
- Hiphop
- Afrohouse
- Dancehall
- Reggaeton
In the attachments you’ll find two backgrounds. One with a lightning bolt , and a grey one with a stroke in the middle. I like both very much , but don’t know which one to choose. That’s why I want to compare the end results of both , and then make a decision. Below you’ll find instructions for both backgrounds.
If you think you can make something better for me , you can also try to do your own thing , and use your own background for example.
Instructions for the first background ( Lightning bolt )
I would like you to design my name ‘Brontel’ into / onto the lightning bolt. I want the lightning bolt + my name to be my DJ Logo , but my name doesn’t have to be in very big letters. Tormenta is the name of the mixtape and has to be in big letters. I was thinking above the logo.
Then there are 2 remaining sentences : ‘Mixed by DJ Brontel’ and ‘Mixtape Volume 1’. These two sentences have to be smaller than ‘Tormenta’. You can put them under the logo.
Instructions for the second background ( Grey )
I would like you to create a logo of my whole name ‘Brontel’ Or just with the letter V. You can put the logo above the stroke.
The mixtape name ‘Tormenta’ has to be in the middle in big letters.
Then there are 2 remaining sentences : ‘Mixed by DJ Brontel’ and ‘Mixtape Volume 1’. These two have to be smaller than ‘Tormenta’ in the middle. I want these sentences below.
Use your imagination with the name Tormenta , the two sentences and the logo. I want it to look professional and unique.
Kind regards ,
Brontel

```html
<!DOCTYPE html>
<html lang="en">
<head>
<meta charset="utf-8">
<title>Tormenta – Mixtape Volume 1</title>
<link rel="stylesheet" href="https://fonts.googleapis.com/css2?family=Metal+Mania&family=Open+Sans:wght@400;600;700&display=swap">
<style>
  :root {
    --bg-dark: #141517;
    --bg-mid: #2a2c30;
    --band: #3a3d42;
    --cyan: #3cc9f7;
    --cyan-glow: #1aa8ff;
    --white: #f4f6f8;
  }
  html, body {
    margin: 0;
    padding: 0;
    width: 1200px;
    height: 1200px;
    overflow: hidden;
    background: var(--bg-dark);
  }
  .cover {
    position: relative;
    width: 1200px;
    height: 1200px;
    overflow: hidden;
    background:
      repeating-linear-gradient(180deg, rgba(255,255,255,0.025) 0 2px, rgba(0,0,0,0.05) 2px 6px),
      radial-gradient(ellipse 75% 60% at 50% 45%, var(--bg-mid) 0%, #1d1e21 60%, var(--bg-dark) 100%);
  }
  .light-band {
    position: absolute;
    left: 0;
    top: 420px;
    width: 1200px;
    height: 130px;
    background: linear-gradient(180deg, rgba(80,84,92,0.0) 0%, rgba(80,84,92,0.55) 40%, rgba(60,63,70,0.35) 100%);
  }
  .glow-line {
    position: absolute;
    left: 50%;
    transform: translateX(-50%);
    width: 760px;
    height: 4px;
    border-radius: 2px;
    background: linear-gradient(90deg, transparent, var(--cyan-glow) 25%, #bfeaff 50%, var(--cyan-glow) 75%, transparent);
    box-shadow: 0 0 30px 8px rgba(26,168,255,0.45), 0 0 90px 30px rgba(26,168,255,0.18);
  }
  .glow-line--top { top: 478px; }
  .glow-line--bottom { top: 708px; }
  .dj-name {
    position: absolute;
    top: 150px;
    left: 0;
    width: 100%;
    text-align: center;
    font-family: "Open Sans", sans-serif;
    font-weight: 700;
    font-size: 64px;
    letter-spacing: 10px;
    color: var(--white);
  }
  .title {
    position: absolute;
    top: 500px;
    left: 0;
    width: 100%;
    text-align: center;
    font-family: "Metal Mania", fantasy;
    font-size: 170px;
    line-height: 180px;
    letter-spacing: 6px;
    color: var(--cyan);
    text-shadow: 0 0 18px rgba(60,201,247,0.35);
  }
  .credits {
    position: absolute;
    left: 0;
    width: 100%;
    text-align: center;
    font-family: "Open Sans", sans-serif;
    color: var(--white);
  }
  .credits--mixed {
    top: 1020px;
    font-size: 34px;
    font-weight: 600;
  }
  .credits--volume {
    top: 1098px;
    font-size: 27px;
    font-weight: 400;
    letter-spacing: 9px;
  }
</style>
</head>
<body>
  <main class="cover">
    <div class="light-band"></div>
    <div class="glow-line glow-line--top"></div>
    <div class="glow-line glow-line--bottom"></div>
    <div class="dj-name">BRONTEL</div>
    <h1 class="title" style="margin:0;font-weight:400;">TORMENTA</h1>
    <p class="credits credits--mixed" style="margin:0;">Mixed by DJ Brontel</p>
    <p class="credits credits--volume" style="margin:0;">Mixtape Volume 1</p>
  </main>
</body>
</html>
```